Our private family owned investment company owns a vineyard in Napa. We want to design a label to put on our wine bottles once wine is ready. We would like artists to develop a creative design for a new label using this wording: Vineyard 48217. The dimensions of the label will be the standard label size on a 750 ml wine bottle. We appreciate creative flair, a classy look, preferably color but open to black and white too; maybe submit both ways. **As more explanation for designers, our family founded and owned a business for over 50 years and our logo was a teal colored snowflake (see attached jpeg logo). Our first plant address was numbered 48217. After our business was sold, our new family office is on located at 48217 Holloway. We have created a new business logo (see attached blue TRV logo) So the 48217 and 2 logos all have lineage and sentimental value to our family. Thank you for providing your unique creativity to this project.

Target Market(s)

to inspire conversation and reminiscing among friends and business associates when entertaining them.

Industry/Entity Type

Investment

Colors

Designer to choose colors to be used in the design.

Requirements
Must have
• Must Incorporate the wording: Vineyard 48217 - as part of the entire design and please see the attached logos (sketch of Vineyard 48217, blue snowflake logo, and TRV logo) and use any of these as a base, or part of, your new design. ** See project description for more detail on the meaning behind these logos.**

```html
<!DOCTYPE html>
<html lang="en">
<head>
<meta charset="utf-8">
<title>Vineyard 48217 — Cabernet Label</title>
<link rel="stylesheet" href="https://fonts.googleapis.com/css2?family=Open+Sans:wght@400;600;700&family=Crimson+Text:wght@400&display=swap">
<style>
  :root {
    --canvas: #ffffff;
    --label-paper: #ffffff;
    --label-edge: #e2e2e2;
    --band-blue: #1b91d1;
    --band-light: #5cbde8;
    --band-deep: #0a86c9;
    --pattern-grey: #d9d9d9;
    --pattern-soft: #ececec;
    --wine-red: #8c1f2b;
    --ink: #3a3a3a;
    --white: #ffffff;
  }
  * { margin: 0; padding: 0; box-sizing: border-box; }
  html, body {
    width: 1200px; height: 1000px; overflow: hidden;
    background: var(--canvas);
  }
  .canvas { position: relative; width: 1200px; height: 1000px; }

  .label {
    position: absolute; left: 120px; top: 110px;
    width: 960px; height: 780px;
    background: var(--label-paper);
    border: 1px solid var(--label-edge);
    overflow: hidden;
  }

  .pattern-top {
    position: absolute; left: 0; top: 0; width: 100%; height: 208px;
    background: linear-gradient(to bottom, var(--label-paper) 0%, var(--pattern-soft) 45%, var(--pattern-grey) 100%);
    opacity: .75;
  }
  .pattern-bottom {
    position: absolute; left: 0; top: 556px; width: 100%; height: 224px;
    background: linear-gradient(to bottom, var(--pattern-grey), var(--pattern-soft));
  }

  .brand-band {
    position: absolute; left: 0; top: 208px; width: 100%; height: 252px;
    background: linear-gradient(to right,
      var(--band-blue) 0%, var(--band-light) 18%, var(--band-blue) 30%,
      var(--band-deep) 42%, var(--band-light) 55%, var(--band-deep) 66%,
      var(--band-blue) 80%, var(--band-deep) 100%);
  }

  .brand-name {
    position: absolute; left: 56px; top: 100px;
    font-family: "Open Sans", sans-serif; font-weight: 400;
    font-size: 44px; letter-spacing: 3px; text-transform: uppercase;
    color: var(--white); display: flex; align-items: center; gap: 16px;
  }
  .brand-mark {
    width: 22px; height: 22px; border-radius: 50%; background: var(--white);
  }

  .info-column {
    position: absolute; left: 738px; top: 28px; width: 200px;
    font-family: "Open Sans", sans-serif; color: var(--white);
  }
  .info-heading {
    font-weight: 700; font-size: 19px; letter-spacing: 3px;
    margin-bottom: 4px;
  }
  .info-text { font-size: 14.5px; line-height: 20px; }
  .info-block + .info-block { margin-top: 28px; }

  .details-strip {
    position: absolute; left: 0; top: 460px; width: 100%; height: 96px;
    background: var(--label-paper);
  }
  .varietal {
    position: absolute; left: 134px; top: 10px;
    font-family: "Crimson Text", serif; font-size: 27px; letter-spacing: 2px;
    color: var(--wine-red);
  }
  .vintage {
    position: absolute; left: 188px; top: 52px;
    font-family: Arial, "Open Sans", sans-serif; font-size: 19px; color: var(--ink);
  }
  .abv, .volume {
    position: absolute; top: 42px;
    font-family: Arial, "Open Sans", sans-serif; font-size: 19px; color: #6a6a6a;
  }
  .abv { left: 618px; }
  .volume { left: 838px; }
</style>
</head>
<body>
<div class="canvas">
  <section class="label">
    <div class="pattern-top" role="img" aria-label="Faint grey repeating snowflake pattern fading upward"></div>

    <div class="brand-band">
      <div class="brand-name"><span>Vineyard 48217</span><span class="brand-mark"></span></div>
      <div class="info-column">
        <div class="info-block">
          <div class="info-heading">CABERNET</div>
          <div class="info-text">Cabernet Sauvignon<br>Estate grown in<br>Napa Valley</div>
        </div>
        <div class="info-block">
          <div class="info-heading">ADDRESS</div>
          <div class="info-text">Vineyard 48217<br>48217 Holloway<br>Napa, CA</div>
        </div>
      </div>
    </div>

    <div class="details-strip">
      <div class="varietal">CABERNET</div>
      <div class="vintage">2017</div>
      <div class="abv">12% vol.</div>
      <div class="volume">750 ml</div>
    </div>

    <div class="pattern-bottom" role="img" aria-label="Light grey repeating snowflake pattern"></div>
  </section>
</div>
</body>
</html>
```